Glow in the Dark Inks Sales Flyer - Targeted to the music industry

We need help!
We need a creative flyer to tell the music industry about our new, colorful glow in the dark inks that look amazing on T-shirts and concert merchandise.

The flyer will go to merchandising managers for bands around the world. The design needs to be hip and contemporary but not offensive. No f-bombs please! Size is 4” x 6” or 3” x 5”, and will be printed on card stock. Design can be both sides if you want. We expect color but black and white with some fluorescent accents could be cool. Surprise us.
Here’s some copy, and we can fill in the contact info when the design is close to final.

Help your fans get lit with branded T-shirts and merchandise that glows in the dark!

Let our new Starwell Pigments light up your next show!

Call us now –
Updates

Hello Designers.

Please keep in mind that although the thought of glow-in-the-dark may trigger a glowing, green color in your creative minds, StarWell Pigments has a wide variety of colors to bring to offer. So please be sure to show that it's not only green glow we are promoting but we have a wide range of colors that glow (including pink, purple, white that glow blue, blue, green, orange, yellow, etc.)

Thank you!

```html
<!DOCTYPE html>
<html lang="en">
<head>
<meta charset="utf-8">
<title>Starwell Pigments – Glow Ink Flyers</title>
<link rel="stylesheet" href="https://fonts.googleapis.com/css2?family=Bangers&family=Anton&family=Crimson+Pro:wght@700&display=swap">
<style>
  :root {
    --page: #ffffff;
    --sky: #1d55f0;
    --ink-dark: #0a0a0a;
    --paper: #ffffff;
    --green: #3aae5e;
    --lime: #c2ee22;
    --yellow: #f8f520;
    --pink: #f224ee;
    --khaki: #a9a070;
    --shirt-top: #2a2f33;
    --shirt-bottom: #0b0b0b;
  }
  * { box-sizing: border-box; margin: 0; padding: 0; }
  html, body { width: 1200px; height: 900px; overflow: hidden; background: var(--page); }
  .canvas { position: relative; width: 1200px; height: 900px; }

  .flyer {
    position: absolute; top: 57px; width: 526px; height: 788px;
    overflow: hidden; background: var(--sky);
  }
  .flyer--yellow { left: 66px; --accent: var(--yellow); --accent-2: var(--lime); }
  .flyer--pink { left: 611px; --accent: var(--pink); --accent-2: var(--khaki); }

  .flyer__art { position: absolute; inset: 0; width: 526px; height: 788px; }
  .shape--accent { fill: var(--accent); }
  .shape--accent-2 { fill: var(--accent-2); }
  .shape--green { fill: var(--green); }

  .shirt-placeholder {
    position: absolute; left: 30px; top: 295px; width: 480px; height: 493px;
    background: linear-gradient(180deg, var(--shirt-top) 0%, var(--shirt-bottom) 35%);
  }

  .brand {
    position: absolute; top: 20px; left: 0; width: 100%;
    text-align: center; font-family: "Bangers", cursive;
    font-size: 72px; line-height: 1; letter-spacing: 1px;
    color: var(--ink-dark); transform: scaleY(1.15);
  }

  .pitch {
    position: absolute; white-space: nowrap;
    font-family: "Anton", sans-serif; font-size: 44px; line-height: 1;
    color: var(--paper); text-transform: uppercase;
    transform-origin: center;
  }
  .pitch--one { left: 250px; top: 290px; transform: translate(-50%, -50%) rotate(-20deg) scaleX(0.66); }
  .pitch--two { left: 298px; top: 390px; transform: translate(-50%, -50%) rotate(-25deg) scaleX(0.66); }

  .band-name {
    position: absolute; top: 500px; left: 0; width: 100%; text-align: center;
    font-family: "Bangers", cursive; font-size: 78px; line-height: 1;
    color: var(--accent);
    text-shadow: 0 0 8px var(--accent), 0 0 18px var(--accent);
  }

  .tagline {
    position: absolute; top: 594px; left: 0; width: 100%; text-align: center;
    font-family: "Crimson Pro", serif; font-weight: 700; font-size: 32px;
    line-height: 41px; color: var(--paper); text-transform: uppercase;
  }

  .cta {
    position: absolute; top: 716px; left: 0; width: 100%; text-align: center;
    font-family: "Bangers", cursive; font-size: 70px; line-height: 1;
    color: var(--paper); letter-spacing: 1px;
  }
</style>
</head>
<body>
<main class="canvas">

  <section class="flyer flyer--yellow">
    <svg class="flyer__art" viewBox="0 0 526 788" aria-hidden="true">
      <polygon class="shape--accent" points="0,150 90,20 140,140 230,50 260,140 330,80 420,40 526,60 526,300 440,330 300,280 180,310 0,320"/>
      <polygon class="shape--accent-2" points="0,180 80,100 160,260 90,300 0,330"/>
      <polygon class="shape--accent-2" points="400,120 470,40 526,120 526,260 440,230"/>
      <polygon class="shape--green" points="0,380 60,330 140,420 0,530"/>
      <polygon class="shape--green" points="420,390 526,330 526,570 470,545"/>
    </svg>
    <div class="shirt-placeholder" role="img" aria-label="Black band T-shirt printed with glow-in-the-dark ink"></div>
    <h1 class="brand">STARWELL PIGMENTS</h1>
    <p class="pitch pitch--one">Help your fans get lit with branded T-shirts</p>
    <p class="pitch pitch--two">and merchandise that glows in the dark!</p>
    <p class="band-name">THE BAND</p>
    <p class="tagline">Let our new Starwell<br>Pigments light up your next<br>show</p>
    <p class="cta">CALL US NOW</p>
  </section>

  <section class="flyer flyer--pink">
    <svg class="flyer__art" viewBox="0 0 526 788" aria-hidden="true">
      <polygon class="shape--accent" points="0,150 90,20 140,140 230,50 260,140 330,80 420,40 526,60 526,300 440,330 300,280 180,310 0,320"/>
      <polygon class="shape--accent-2" points="0,180 80,100 160,260 90,300 0,330"/>
      <polygon class="shape--accent-2" points="400,200 470,150 526,200 526,300 440,310"/>
      <polygon class="shape--green" points="0,380 60,330 140,420 0,530"/>
      <polygon class="shape--green" points="420,390 526,330 526,570 470,545"/>
    </svg>
    <div class="shirt-placeholder" role="img" aria-label="Black band T-shirt printed with glow-in-the-dark ink"></div>
    <h1 class="brand">STARWELL PIGMENTS</h1>
    <p class="pitch pitch--one">Help your fans get lit with branded T-shirts</p>
    <p class="pitch pitch--two">and merchandise that glows in the dark!</p>
    <p class="band-name">THE BAND</p>
    <p class="tagline">Let our new Starwell<br>Pigments light up your next<br>show</p>
    <p class="cta">CALL US NOW</p>
  </section>

</main>
</body>
</html>
```